Savour and Thrive Wellbeing is being Launched and needs a business card and stationery package

I need a stationery package including business card (primary focus) , letterhead, digital letterhead, envelopes, with compliments slip, A 5 note sheet for the rebranding of my business and launch of my new website. I have a logo, like beige, brown earthy tones with a hint of red. I would also like the option of my letterhead also being printed on recycled paper in another format as well as the traditional letterhead. I do also send my letters to GPs and specialists digitally as well. I like to stand out from the usual stereotype of fruits and vegetables on business cards as I find that quite tacky and stereotypical. I want the business card to capture the essence of my logo as natural, nutrition, enjoyment, nurturing and freedom with food. I have attached the logo, and additional brief sheet on my ideas. Happy to have any background that is complementary to my theme, and what you believe would be catching. Definitely DONT'T like pink, try to pick up the darker colour in the logo please. and think too much black is a little overpowering.

Target Market(s)

clients who are interested in improving their health and wellness. Client 80% females; 20% males

Industry/Entity Type

Health And Wellness

Contact Information for Business Card

I am open to having different backgrounds as well that would complement the logo. Probably less emphasis on the heart out of the logo - just happy to keep that in the logo only please
I am also wanting two business cards - one for the appointments, one for general distribution and media distribution (both need to look consistent though) - but does give opportunity for one of the business cards to be less wordy and more striking. And the front of the business card can certainly stand out with the entire savour and thrive logo and my name and grab the attention of the receiver.
1st business card
on front:
Lorena Whitcombe
Savour and Thrive Wellbeing & logo
Nutritionist and Dietitian
Tarvel Medical Centre
647 Brindle Hill Rd, Quorrel Q 4987
Phone: (07) 3017 2968 Fax: (07) 3156 7209
Mobile: 0400 261 937
www.savourandthrivewellbeing.example.au
lorena@savourandthrivewellbeing.example.au
on back:
next appointment

……………………….. at ……………………… (possibly 4 times)
If you are unable to keep your appointment, please contact us as soon as possible (small font)
2nd business card (needs to be very eye catching and stand out)
on front: Savour and Thrive Wellbeing logo and my name
on back:
Lorena Whitcombe
address
phones, fax, website, email address

Font styles to use
Other font styles liked:
• please refer to logo

Requirements
Must have
• refreshing and simple; new and vibrant - I am rebranding my business after 20 years
• to get a feel of what is the theme - go to my new website (not completed as yet - but you will get a preliminary view) - don't do as google search as blocked - but can put into website header and it will be shown
• www.savourandthrivewellbeing.example.au - but please ignore the colouring of the 4 blocks under the slider on the home page - I am not wanting these colourings - they are getting updated.
Nice to have
• earthy tones, beige, hint of red, fonts to match logo if possible, organic, modern
• get inspiration from my logo please, open to having other backgrounds that complement
Should not have
• no food shots or stereotypical weight/ scales images
• no green, yellow or orange

```html
<!DOCTYPE html>
<html lang="en">
<head>
<meta charset="utf-8">
<title>Savour and Thrive Wellbeing – Business Card</title>
<link rel="stylesheet" href="https://fonts.googleapis.com/css2?family=Arimo:wght@400;700&display=swap">
<style>
  :root {
    --bg: #ece7e1;
    --berry: #9b3454;
    --berry-deep: #862a47;
    --berry-light: #a9405f;
    --paper: #ffffff;
    --ink: #3a3a3a;
    --rule: #8a8a8a;
    --accent-red: #b02a46;
  }
  * { box-sizing: border-box; margin: 0; padding: 0; }
  html, body { width: 1200px; height: 950px; overflow: hidden; }
  body {
    background: var(--bg);
    font-family: "Arimo", Arial, sans-serif;
    position: relative;
  }

  .card {
    position: absolute;
    box-shadow: 0 10px 28px rgba(60, 40, 30, 0.22);
    border-radius: 4px;
    overflow: hidden;
  }

  /* Front card */
  .card-front {
    left: 90px; top: 135px;
    width: 420px; height: 680px;
    background: linear-gradient(160deg, var(--berry-light) 0%, var(--berry) 55%, var(--berry-deep) 100%);
    color: #fff;
  }
  .contact {
    position: absolute;
    right: 38px; top: 48px;
    text-align: right;
    line-height: 1.5;
    font-size: 15px;
  }
  .contact .name { font-size: 24px; font-weight: 700; line-height: 1.25; }
  .contact .role { font-size: 17px; margin-bottom: 16px; }
  .contact .label { font-weight: 700; }
  .contact .web { font-weight: 700; }
  .front-mark {
    position: absolute;
    left: -60px; bottom: -40px;
    width: 340px; height: 340px;
  }

  /* Back card */
  .card-back {
    left: 560px; top: 290px;
    width: 580px; height: 360px;
    background: var(--paper);
    color: var(--ink);
    padding: 34px 40px;
  }
  .brand {
    display: flex; align-items: center; gap: 12px;
    color: var(--ink);
    font-size: 20px;
    font-weight: 400;
  }
  .brand-dot {
    width: 16px; height: 16px; border-radius: 50%;
    background: var(--accent-red);
  }
  .appointment-title {
    position: absolute; right: 40px; top: 40px;
    color: var(--accent-red);
    font-weight: 700; font-size: 16px;
    letter-spacing: 0.03em;
  }
  .appointment-lines {
    list-style: none;
    margin-top: 46px;
  }
  .appointment-lines li {
    display: flex; align-items: flex-end; gap: 8px;
    font-size: 13px; color: var(--ink);
    height: 46px;
  }
  .appointment-lines .fill {
    flex: 1;
    border-bottom: 1.5px dotted var(--rule);
    margin-bottom: 3px;
  }
  .appointment-lines .fill.time { flex: 0.6; }
  .notice {
    position: absolute; left: 40px; bottom: 26px;
    font-size: 12px; font-style: italic; color: var(--ink);
  }
</style>
</head>
<body>

  <section class="card card-front" aria-label="Business card front">
    <div class="contact">
      <p class="name">Lorena Whitcombe</p>
      <p class="role">Nutritionist and Dietitian</p>
      <p>Tarvel Medical Centre</p>
      <p>647 Brindle Hill Rd, Quorrel Q 4987</p>
      <p><span class="label">P</span> : (07) 3017 2968</p>
      <p><span class="label">M</span> : (07) 3156 7209 <span class="label">F</span> : 0400 261 937</p>
      <p>lorena@savourandthrivewellbeing.example.au</p>
      <p class="web">www.savourandthrivewellbeing.example.au</p>
    </div>
    <svg class="front-mark" viewBox="0 0 340 340" aria-hidden="true">
      <circle cx="170" cy="170" r="160" fill="#ffffff" opacity="0.9"/>
    </svg>
  </section>

  <section class="card card-back" aria-label="Business card back">
    <div class="brand">
      <span class="brand-dot"></span>
      <span>Savour and Thrive Wellbeing</span>
    </div>
    <p class="appointment-title">NEXT APPOINTMENT</p>
    <ul class="appointment-lines">
      <li><span class="fill"></span><span>at</span><span class="fill time"></span></li>
      <li><span class="fill"></span><span>at</span><span class="fill time"></span></li>
      <li><span class="fill"></span><span>at</span><span class="fill time"></span></li>
    </ul>
    <p class="notice">If you are unable to keep your appointment, please contact us as soon as possible</p>
  </section>

</body>
</html>
```